Dovamel Nutrition Supplement Jar

Label for jar. White label on a brown bottle jar.
Conservative look, should look like medicine.
Main Side:
Oak Harbor Clinics (smaller size) (with logo)
DOVAMEL 10mg (large size)
Doctor Formulated
Developed in Clinical Practice
60 Capsules
(I prefer the single color white label with dark brown letters. Please stay close to that design)
(For the back side, please use the multicolor set up)
(The whole Label should be one color - white with dark brown letters)
Please visit my site for more inspiration and feel: www.velmorine.example
The product will be brown jar listed on this site.
Can you please provide one version without the text "Oak Harbor Clinics & Logo".
Thank you.

Target Market(s)

Women, 34-59 years old

Industry/Entity Type

Nutrition

Requirements
Should not have
• Multicolors, leaves,

```html
<!DOCTYPE html>
<html lang="en">
<head>
<meta charset="utf-8">
<title>Dovamel 10mg – Jar Label</title>
<link rel="stylesheet" href="https://fonts.googleapis.com/css2?family=Roboto:wght@300;400;500&family=Barlow:wght@300;600&display=swap">
<style>
  :root {
    --page-bg: #e6e6e6;
    --label-white: #ffffff;
    --gold: #d2ad52;
    --gold-soft: #dcbd6e;
    --gold-dark: #a47d2c;
    --band-light: #e9c978;
    --band-mid: #c9a24c;
    --band-text: #ffffff;
  }
  html, body {
    margin: 0;
    padding: 0;
    width: 1067px;
    height: 1200px;
    overflow: hidden;
    background: var(--page-bg);
  }
  .label {
    position: absolute;
    left: 103px;
    top: 105px;
    width: 860px;
    height: 990px;
    background: var(--label-white);
    font-family: "Roboto", Arial, sans-serif;
    color: var(--gold);
  }
  .centered {
    position: absolute;
    left: 0;
    width: 100%;
    text-align: center;
  }
  .brand-mark {
    position: absolute;
    left: 371px;
    top: 84px;
    width: 118px;
    height: 118px;
  }
  .brand-name {
    top: 238px;
    font-size: 66px;
    font-weight: 500;
    line-height: 1;
    letter-spacing: 0.5px;
  }
  .brand-rule {
    position: absolute;
    left: 85px;
    top: 323px;
    width: 676px;
    height: 2px;
    background: var(--gold);
  }
  .clinic-name {
    top: 338px;
    font-size: 27px;
    font-weight: 300;
    line-height: 1;
  }
  .product-band {
    position: absolute;
    left: 142px;
    top: 435px;
    width: 562px;
    height: 73px;
    background: linear-gradient(90deg, var(--gold-dark) 0%, var(--band-light) 25%, var(--band-mid) 60%, var(--gold-dark) 100%);
    display: flex;
    align-items: center;
    justify-content: center;
  }
  .product-name {
    font-family: "Barlow", Arial, sans-serif;
    font-weight: 600;
    font-size: 58px;
    letter-spacing: 2px;
    color: var(--band-text);
    line-height: 1;
  }
  .claims {
    top: 615px;
    font-size: 22px;
    font-weight: 300;
    line-height: 31px;
    letter-spacing: 1.5px;
    color: var(--gold-soft);
    margin: 0;
  }
  .capsule-count {
    top: 892px;
    font-family: "Barlow", Arial, sans-serif;
    font-size: 32px;
    font-weight: 300;
    line-height: 1;
    letter-spacing: 0.5px;
    margin: 0;
  }
  .capsule-count strong { font-weight: 600; }
  .count-rule {
    position: absolute;
    left: 302px;
    top: 942px;
    width: 234px;
    height: 3px;
    background: var(--gold);
  }
</style>
</head>
<body>
  <main class="label">
    <svg class="brand-mark" viewBox="0 0 118 118" aria-hidden="true">
      <circle cx="59" cy="59" r="56" fill="none" stroke="var(--gold)" stroke-width="3"/>
    </svg>
    <div class="centered brand-name">Velmorine</div>
    <div class="brand-rule"></div>
    <div class="centered clinic-name">Oak Harbor Clinics</div>

    <div class="product-band">
      <span class="product-name">DOVAMEL 10mg</span>
    </div>

    <p class="centered claims">DOCTOR FORMULATED<br>DEVELOPED IN CLINICAL PRACTICE</p>

    <p class="centered capsule-count"><strong>60</strong> Capsules</p>
    <div class="count-rule"></div>
  </main>
</body>
</html>
```